ALL TYPES OF COMMERCIAL PLASTERING

TYPE OF BLOCK LETTERING WITH STAND OUT QUALITIES
WITH SOME TYPE OF LOGO
SOMETHING UNIQUE FOR THE BUILDING INDUSTRY.
QUALITY WORKMANSHIP
Updates

forgot to include my mobile phone number on my brief. could you add it to your design please MOBILE PH 0412 858 196

please let me make this quite clear ,the company name is harbourline linings and Fitouts PTY LTD. THE TYPE OF WORK WE WILL BE DOING IS COMMERCIAL PLASTERING.

Industry/Entity Type

Industry

Contact Information for Business Card

harbourline linings and fitouts P/L
marcus devlin p.o.box 42 wendouree 3355 email address harbourlinelinings@examplemail.com
ABN 51 718 294 605 COMMERCIAL PLASTERING

```html
<!DOCTYPE html>
<html lang="en">
<head>
<meta charset="utf-8">
<title>Harbourline Linings and Fitouts – Business Card</title>
<link rel="stylesheet" href="https://fonts.googleapis.com/css2?family=Open+Sans:wght@400;600;700&display=swap">
<style>
  :root {
    --backdrop: #e9e6e1;
    --card-white: #fafafa;
    --card-shade: #e4e4e4;
    --brand-blue: #1f64a8;
    --brand-blue-deep: #14487f;
    --brand-red: #e21f32;
    --ink-grey: #555a5f;
    --ink-soft: #7b8086;
    --paper: #ffffff;
  }
  * { box-sizing: border-box; margin: 0; padding: 0; }
  html, body {
    width: 1200px;
    height: 1023px;
    overflow: hidden;
    background: var(--backdrop);
    font-family: "Open Sans", Arial, sans-serif;
  }
  .stage { position: relative; width: 1200px; height: 1023px; }

  .card {
    position: absolute;
    width: 540px;
    height: 309px;
    border-radius: 4px;
    overflow: hidden;
    box-shadow: 0 10px 28px rgba(0,0,0,0.22);
  }

  /* Front */
  .card-front {
    left: 60px; top: 150px;
    background: linear-gradient(160deg, var(--paper), var(--card-white) 60%, var(--card-shade));
  }
  .card-front .sweep { position: absolute; inset: 0; }
  .brand-row {
    position: absolute; left: 30px; top: 22px;
    display: flex; align-items: center; gap: 14px;
  }
  .brand-dot {
    width: 44px; height: 44px; border-radius: 50%;
    background: var(--brand-blue);
  }
  .brand-name {
    font-size: 15px; font-weight: 600; letter-spacing: 1.5px;
    color: var(--ink-grey); text-transform: uppercase;
  }
  .brand-service {
    position: absolute; left: 88px; top: 58px;
    font-size: 23px; font-weight: 600; letter-spacing: 0.5px;
    color: var(--ink-grey); text-transform: uppercase;
    white-space: nowrap;
  }
  .holder {
    position: absolute; left: 120px; top: 228px; height: 28px;
    transform: rotate(-17deg); transform-origin: left center;
    display: flex; align-items: center; gap: 10px;
    color: var(--paper); white-space: nowrap;
  }
  .holder-name { font-size: 21px; font-weight: 700; letter-spacing: 0.3px; line-height: 28px; }
  .holder-divider { width: 3px; height: 22px; background: var(--paper); }
  .holder-role { font-size: 13px; font-weight: 400; }
  .contact {
    position: absolute; left: 300px; top: 222px;
    transform: rotate(-17deg); transform-origin: left top;
    list-style: none; white-space: nowrap;
    font-size: 12px; line-height: 17px; color: var(--ink-soft);
    letter-spacing: 0.4px;
  }
  .contact .gap { margin-top: 6px; }

  /* Back */
  .card-back {
    left: 600px; top: 560px;
    background: radial-gradient(ellipse at 45% 40%, #2a74ba, var(--brand-blue) 45%, var(--brand-blue-deep));
  }
  .card-back .sweep { position: absolute; inset: 0; }
  .back-mark {
    position: absolute; left: 0; right: 60px; top: 104px;
    display: flex; align-items: center; justify-content: center; gap: 14px;
  }
  .back-mark .brand-dot { width: 60px; height: 60px; background: var(--paper); }
  .back-mark .brand-name { color: var(--paper); font-size: 18px; }
  .back-service {
    position: absolute; left: 34px; bottom: 30px;
    font-size: 24px; font-weight: 600; letter-spacing: 0.6px;
    color: var(--paper); text-transform: uppercase;
  }
  .abn {
    position: absolute; right: 14px; bottom: 14px;
    transform: rotate(-90deg) translate(100%, 0); transform-origin: right bottom;
    font-size: 10px; letter-spacing: 0.6px; color: var(--brand-blue-deep);
    white-space: nowrap;
  }
</style>
</head>
<body>
<main class="stage">

  <section class="card card-front" aria-label="Business card front">
    <svg class="sweep" width="540" height="309" viewBox="0 0 540 309" aria-hidden="true">
      <path d="M0,236 L540,76 L540,86 L0,248 Z" fill="var(--brand-blue)"/>
      <path d="M0,256 L540,92 L540,136 L0,302 Z" fill="var(--brand-red)"/>
    </svg>
    <div class="brand-row">
      <span class="brand-dot"></span>
      <span class="brand-name">Harbourline</span>
    </div>
    <h1 class="brand-service">Commercial Plastering</h1>
    <div class="holder">
      <span class="holder-name">Marcus Devlin</span>
      <span class="holder-divider"></span>
      <span class="holder-role">Director</span>
    </div>
    <ul class="contact">
      <li>0412 858 196</li>
      <li>harbourlinelinings@examplemail.com</li>
      <li class="gap">harbourline linings and fitouts P/L</li>
      <li>p.o.box 42 wendouree 3355</li>
    </ul>
  </section>

  <section class="card card-back" aria-label="Business card back">
    <svg class="sweep" width="540" height="309" viewBox="0 0 540 309" aria-hidden="true">
      <path d="M470,0 C440,90 440,220 475,309 L540,309 L540,0 Z" fill="var(--brand-red)"/>
    </svg>
    <div class="back-mark">
      <span class="brand-dot"></span>
      <span class="brand-name">Harbourline</span>
    </div>
    <p class="back-service">Commercial Plastering</p>
    <p class="abn">ABN 51 718 294 605</p>
  </section>

</main>
</body>
</html>
```